Bar and Grill needs specials signage

I have attached a file called "daily specials" I need it changed - so there is 1 sign/poster for each day/special
also attached other items to show some styling. I want the new posters chalkboard format, styled along the lines of the drink designs attached.
The designs should be scaleable, and editable, I will print locally

```html
<!DOCTYPE html>
<html lang="en">
<head>
<meta charset="utf-8">
<title>Daily Specials – Thursday</title>
<link rel="stylesheet" href="https://fonts.googleapis.com/css2?family=Fredericka+the+Great&family=Cabin+Sketch:wght@400;700&family=Yellowtail&family=Gochi+Hand&display=swap">
<style>
  :root {
    --board-dark: #232723;
    --board-mid: #3a3f3a;
    --board-light: #575c57;
    --chalk: #f4f4f0;
    --chalk-soft: rgba(244, 244, 240, 0.85);
    --orange: #f0791f;
    --yellow: #d8cf2c;
  }
  * { margin: 0; padding: 0; box-sizing: border-box; }
  html, body { width: 927px; height: 1200px; overflow: hidden; background: var(--board-dark); }
  .poster {
    position: relative;
    width: 927px;
    height: 1200px;
    overflow: hidden;
    background:
      radial-gradient(ellipse 55% 45% at 50% 58%, var(--board-light) 0%, var(--board-mid) 45%, transparent 80%),
      radial-gradient(ellipse 70% 60% at 50% 50%, var(--board-mid) 0%, var(--board-dark) 100%);
    color: var(--chalk);
  }
  .chalk-art { position: absolute; inset: 0; width: 927px; height: 1200px; }
  .frame { fill: none; stroke: var(--chalk); stroke-width: 4; stroke-linejoin: round; }
  .frame-inner { fill: none; stroke: var(--chalk-soft); stroke-width: 1.5; }
  .rule { stroke: var(--chalk); stroke-width: 4; stroke-linecap: round; }
  .accent-dash { stroke: var(--yellow); stroke-width: 3; stroke-linecap: round; }
  .pointer { fill: none; stroke: var(--yellow); stroke-width: 2.5; stroke-linejoin: round; }

  .heading {
    position: absolute; left: 0; width: 100%; text-align: center;
    font-family: "Fredericka the Great", cursive;
    font-size: 74px; letter-spacing: 2px; top: 78px; line-height: 1;
  }
  .day {
    position: absolute; left: 0; width: 100%; text-align: center;
    font-family: "Yellowtail", cursive;
    font-size: 168px; top: 150px; line-height: 1;
  }
  .special-title {
    position: absolute; left: 0; width: 100%; text-align: center;
    font-family: "Cabin Sketch", cursive; font-weight: 700;
    font-size: 58px; letter-spacing: 3px; top: 422px; line-height: 1;
    color: var(--orange);
  }
  .illustration {
    position: absolute;
    border-radius: 50%;
    background: radial-gradient(ellipse at 50% 50%, rgba(244,244,240,0.28) 0%, rgba(244,244,240,0.12) 55%, rgba(244,244,240,0) 75%);
  }
  .illustration--pizza { left: 152px; top: 520px; width: 624px; height: 280px; }
  .illustration--wing-left { left: 204px; top: 952px; width: 172px; height: 156px; }
  .illustration--wing-right { left: 556px; top: 952px; width: 172px; height: 156px; }
  .offer {
    position: absolute; left: 0; width: 100%; text-align: center;
    font-family: "Gochi Hand", cursive;
    font-size: 52px; line-height: 54px; top: 830px;
  }
  .offer-free {
    position: absolute; left: 0; width: 100%; text-align: center;
    font-family: "Cabin Sketch", cursive; font-weight: 700;
    font-size: 66px; letter-spacing: 3px; top: 965px; line-height: 1;
    color: var(--orange);
  }
</style>
</head>
<body>
<main class="poster">
  <svg class="chalk-art" viewBox="0 0 927 1200" aria-hidden="true">
    <rect class="frame" x="44" y="34" width="840" height="1134" rx="4"/>
    <rect class="frame-inner" x="52" y="42" width="824" height="1118" rx="3"/>

    <line class="accent-dash" x1="106" y1="188" x2="132" y2="196"/>
    <line class="accent-dash" x1="88" y1="258" x2="128" y2="258"/>
    <line class="accent-dash" x1="104" y1="330" x2="130" y2="324"/>
    <line class="accent-dash" x1="796" y1="196" x2="822" y2="188"/>
    <line class="accent-dash" x1="806" y1="258" x2="846" y2="258"/>
    <line class="accent-dash" x1="798" y1="324" x2="824" y2="330"/>

    <line class="rule" x1="178" y1="376" x2="776" y2="376"/>
    <line class="rule" x1="152" y1="404" x2="608" y2="404"/>
    <line class="rule" x1="152" y1="500" x2="774" y2="500"/>

    <path class="pointer" d="M826 482 L834 490 L790 548 L800 556 L766 576 L770 538 L780 546 Z"/>
    <path class="pointer" d="M90 716 L120 712 L150 770 L158 762 L158 806 L124 788 L134 782 Z"/>
  </svg>

  <h1 class="heading">DAILY SPECIALS</h1>
  <h2 class="day">Thursday</h2>
  <p class="special-title">PIZZA AND WINGS</p>

  <div class="illustration illustration--pizza" role="img" aria-label="Chalk sketch of a sliced pizza with one slice pulled out"></div>

  <p class="offer">Buy any large pizza and get<br>10 boneless wings</p>

  <div class="illustration illustration--wing-left" role="img" aria-label="Chalk sketch of a chicken wing"></div>
  <p class="offer-free">FREE</p>
  <div class="illustration illustration--wing-right" role="img" aria-label="Chalk sketch of a chicken wing"></div>
</main>
</body>
</html>
```